Bed Company needs business card

Hello, we are a bed company that makes specialized magnets for beds. We are an alternative healing company. I need a modern and upscale business card. Please incorporate my logo for the card.

Accepted file formats are AI, EPS, and Press-Ready PDFS.

Please include all fonts or convert them to outlines regardless of file type.

If you are designing the card in Photoshop the file Must be 1200dpi.

I am open to anything for the business card.  I really like all of your designs and if you want to change the color of the logo, you can.  I will be making the final selection by Friday.  Thank You for all of your designs.  Feel Free to submit different color logos if you want.  

Reason: I will make a decision Final on Friday April 20th. 2012. Good Luck and Thank you all for the designs.

Target Market(s)

My target Market is people, who are looking for alternative healing.

Industry/Entity Type

Business

Requirements
Must have
• My logo must be incorporated. The front card must have

Name
Job Title

Address
Work
Cell
Fax
email
web

Just put in fake info for the card.

The back of the card. I want the logo on the back with color. I just want it to look modern and cool.

```html
<!DOCTYPE html>
<html lang="en">
<head>
<meta charset="utf-8">
<title>Restwell Coil – Business Card</title>
<link rel="stylesheet" href="https://fonts.googleapis.com/css2?family=Mulish:wght@400;600;700&display=swap">
<style>
  :root {
    --backdrop: #ece8e1;
    --card: #f7f7f7;
    --green-dark: #0d6b35;
    --green-bright: #16a346;
    --green-text: #17803d;
    --ink: #3a3a3a;
  }
  * { margin: 0; padding: 0; box-sizing: border-box; }
  html, body {
    width: 1200px; height: 1200px; overflow: hidden;
    background: var(--backdrop);
    font-family: "Mulish", "Helvetica Neue", Arial, sans-serif;
  }
  .card {
    position: absolute; left: 206px; width: 808px; height: 448px;
    background: var(--card);
    border-radius: 14px;
    box-shadow: 0 3px 8px rgba(0,0,0,0.18);
    overflow: hidden;
  }
  .card-front { top: 152px; }
  .card-back { top: 623px; }

  .name-band {
    position: absolute; left: 0; right: 0; top: 173px; height: 87px;
    background: var(--green-dark);
    border-top: 5px solid var(--green-bright);
    border-bottom: 5px solid var(--green-bright);
    display: flex; align-items: center; justify-content: center;
    color: #fff;
  }
  .person-name { font-size: 28px; font-weight: 600; letter-spacing: 0.2px; }
  .divider { width: 2px; height: 34px; background: #fff; margin: 0 13px; }
  .job-title { font-size: 24px; font-weight: 400; }

  .contact {
    position: absolute; left: 0; right: 0; top: 305px;
    text-align: center; color: var(--ink);
    font-size: 16px; line-height: 25.5px;
  }
  .contact .label { color: var(--green-text); font-weight: 700; }
  .contact .gap { display: inline-block; width: 16px; }

  .brand {
    position: absolute; left: 165px; top: 118px;
    display: flex; align-items: center; gap: 22px;
  }
  .brand-mark { width: 70px; height: 70px; background: var(--green-dark); }
  .brand-name {
    font-size: 56px; font-weight: 700; color: var(--green-text);
    line-height: 1;
  }
  .brand-tagline {
    position: absolute; left: 400px; top: 256px;
    font-size: 20px; letter-spacing: 3px; color: var(--green-text);
  }
</style>
</head>
<body>
  <section class="card card-front">
    <div class="name-band">
      <span class="person-name">Daniel Harper</span>
      <span class="divider"></span>
      <span class="job-title">Chief Executive Officer</span>
    </div>
    <div class="contact">
      <div>4810 E Canyon Ridge Dr&nbsp; Mesa, Arizona 85215</div>
      <div><span class="label">Phone.</span> 1-555-208-4417<span class="gap"></span><span class="label">Mobile.</span> 1-555-208-4490</div>
      <div><span class="label">Email.</span> daniel@restwellcoil.com<span class="gap"></span><span class="label">Website.</span> www.restwellcoil.com</div>
    </div>
  </section>

  <section class="card card-back">
    <div class="brand">
      <span class="brand-mark"></span>
      <span class="brand-name">Restwell Coil</span>
    </div>
    <div class="brand-tagline">Alternative Healing</div>
  </section>
</body>
</html>
```